ZEPRILO.COM is a premium domain sales company. Our competitors are companies like vastplots.example, getparcels.example, peerwords.example. Our current site is at www.zeprilos.example.

We want to have the ability to search for domains, to highlight special offers and have some testimonials on the index page.

The logo for the site is attached.

Please be sure that the order form fits on the screen without scrolling the page. I want the entire form, including the submit button to fit without any page scrolling.

Delivered product - INDEX PAGE, ORDER FORM AND CONTENT PAGE PSDs.

Target Market(s)

Small to Medium business professionals

Industry/Entity Type

It Company

Requirements
Must have
• 1. List of domains for sale
2. Simple search box with button to run the search
3. link for advanced search
4. testimonial area. Note - this can be a small box where a different testimonial is displayed on each page load.
Nice to have
• Would like the site to have some white space. Don't want a heavily packed website. Give it an "airy" feel.

```html
<!DOCTYPE html>
<html lang="en">
<head>
<meta charset="utf-8">
<title>ZEPRILO.COM – Premium Domains</title>
<link href="https://fonts.googleapis.com/css2?family=Open+Sans:ital,wght@0,400;0,600;0,700;1,400&family=Roboto+Condensed:wght@400;700&family=Amaranth&display=swap" rel="stylesheet">
<style>
:root{
  --teal-dark:#1a5872;
  --teal:#3b8399;
  --teal-light:#5a9fb2;
  --green:#8ab528;
  --green-dark:#6f9a1c;
  --blue:#0f5a9a;
  --navy:#1d3f5c;
  --orange:#f07c12;
  --text:#333;
  --muted:#666;
  --line:#d9d9d9;
}
*{margin:0;padding:0;box-sizing:border-box}
html,body{width:1120px;height:1200px;overflow:hidden;background:#fff}
body{font-family:"Open Sans",sans-serif;color:var(--text);position:relative}
.abs{position:absolute}

/* header */
.site-header{position:absolute;left:0;top:0;width:1120px;height:90px;border-bottom:3px solid var(--green)}
.brand{left:182px;top:32px;font-weight:700;font-size:26px;color:var(--blue);letter-spacing:-0.5px;display:flex;align-items:center;gap:7px}
.brand-dot{width:12px;height:12px;border-radius:50%;background:var(--green)}
.header-phone{left:440px;top:33px;display:flex;align-items:center;gap:7px;font-size:18px;font-weight:600;color:#444}
.phone-icon{width:24px;height:24px;border-radius:4px;background:var(--green);display:flex;align-items:center;justify-content:center}
.main-nav{left:682px;top:0;display:flex;align-items:flex-start;font-size:13px;color:#666}
.main-nav a{color:#666;text-decoration:none;display:block;padding-top:41px;height:90px}
.main-nav .active{background:var(--teal-dark);color:#fff;width:56px;text-align:center}
.main-nav .sep{color:#bbb;padding:41px 12px 0}
.main-nav .first-sep{padding-left:6px}

/* hero */
.hero{left:0;top:90px;width:1120px;height:438px;background:radial-gradient(ellipse at 45% 35%,#5d9fb1 0%,#3c8399 45%,#1f5f75 100%);overflow:hidden}
.hero-floor{left:0;top:318px;width:1120px;height:120px;background:linear-gradient(#b8c7cc 0,#98aeb5 6px,#6f8f98 10px,#5f8592 60%,#557c89 100%)}
.hero-art{left:744px;top:2px;width:248px;height:388px;background:linear-gradient(160deg,#eef3f4 0%,#d6e2e5 55%,#b9cdd3 100%)}
.hero-title{left:184px;top:106px;color:#fff;font-family:"Roboto Condensed",sans-serif;font-weight:400;font-size:44px;line-height:1;letter-spacing:.2px}
.hero-sub{left:184px;top:144px;color:#fff;font-weight:700;font-size:24px;line-height:1.2}
.search{left:184px;top:180px;width:527px;height:56px;background:linear-gradient(#fff,#eeeeee);border-radius:3px}
.search-input{left:12px;top:14px;font-family:"Amaranth",sans-serif;font-size:19px;color:#666}
.tld-select{left:332px;top:7px;width:91px;height:43px;background:linear-gradient(#eee,#d8d8d8);border:1px solid #ccc;border-radius:2px;font-family:"Amaranth",sans-serif;font-size:19px;color:#555;padding:9px 0 0 12px}
.search-btn{left:430px;top:7px;width:91px;height:43px;background:linear-gradient(#97c534,#6c9a1c);border-radius:2px;display:flex;align-items:center;justify-content:center}
.adv-link{left:185px;top:242px;color:#fff;font-weight:700;font-size:13px}

/* offer */
.offer{left:182px;top:505px;width:740px;height:46px;background:var(--teal-dark)}
.offer-label{left:0;top:0;height:46px;width:206px;background:var(--green);color:#fff;font-weight:700;font-size:14.5px;padding:13px 0 0 14px;clip-path:polygon(0 0,196px 0,206px 23px,196px 46px,0 46px)}
.offer-text{left:232px;top:14px;color:#fff;font-size:14px}
.offer-btn{left:552px;top:6px;width:180px;height:34px;background:linear-gradient(#9cc93c,#78a624);border-radius:2px;color:#1d3a05;font-weight:700;font-size:13.5px;text-align:center;padding-top:7px}

/* listings */
.section-title{left:182px;top:582px;font-size:27px;font-weight:600;color:var(--blue)}
.domain-table{left:186px;top:622px;width:460px;border-collapse:collapse}
.domain-table th{font-size:11.5px;font-weight:600;color:#333;text-align:left;height:20px;padding:0}
.domain-table td{height:32px;font-size:13.5px;padding:0}
.domain-table td.name{font-weight:700;color:#333;width:202px}
.domain-table td.cat{color:#555;width:115px}
.domain-table td.price{color:var(--orange);width:94px}
.buy{display:block;width:48px;height:24px;background:linear-gradient(#f4f4f4,#d9d9d9);border:1px solid #c4c4c4;border-radius:2px;font-size:11px;font-weight:700;color:#666;text-align:center;line-height:22px}
.pager{left:186px;top:1038px;width:459px;height:32px;border:1px solid var(--line);border-radius:2px;background:linear-gradient(#fff,#f3f3f3);text-align:center;font-size:12.5px;color:#777;padding-top:7px}
.pager b{font-weight:400;color:var(--blue)}

/* testimonial */
.testi-title{left:688px;top:592px;font-size:14px;font-weight:700;color:var(--green)}
.quote-mark{left:690px;top:621px}
.testi-who{left:745px;top:648px;font-size:13px;color:#555}
.testi-who span{color:var(--blue)}
.testi-text{left:691px;top:678px;width:222px;font-style:italic;font-size:13px;line-height:19.2px;color:var(--navy)}

/* footer */
.site-footer{left:0;top:1122px;width:1120px;height:78px;background:linear-gradient(#a9c94a,#80ae2e);border-top:2px solid #dfe9c6}
.foot-links{left:193px;top:22px;font-size:11.5px;color:#fff;display:flex;gap:12px}
.foot-copy{left:193px;top:38px;font-size:11.5px;color:var(--navy)}
.foot-addr{left:525px;top:20px;font-size:11.5px;color:#fff;line-height:15.5px}
.foot-phone{left:797px;top:18px;font-size:19px;font-weight:600;color:var(--navy)}
</style>
</head>
<body>

<header class="site-header">
  <div class="abs brand"><span>ZEPRILO.COM</span><span class="brand-dot"></span></div>
  <div class="abs header-phone">
    <span class="phone-icon"><svg width="14" height="14" viewBox="0 0 24 24"><path fill="#fff" d="M6.6 10.8a15.1 15.1 0 0 0 6.6 6.6l2.2-2.2c.3-.3.7-.4 1-.2 1.1.4 2.3.6 3.6.6.6 0 1 .4 1 1V20c0 .6-.4 1-1 1A17 17 0 0 1 3 4c0-.6.4-1 1-1h3.5c.6 0 1 .4 1 1 0 1.3.2 2.5.6 3.6.1.3 0 .7-.2 1z"/></svg></span>
    +1 555.014.2290
  </div>
  <nav class="abs main-nav">
    <a class="active" href="#">Home</a>
    <span class="sep first-sep">|</span><a href="#">FAQS</a>
    <span class="sep">|</span><a href="#">About Us</a>
    <span class="sep">|</span><a href="#">Contact</a>
  </nav>
</header>

<section class="abs hero">
  <div class="abs hero-floor"></div>
  <div class="abs hero-art" role="img" aria-label="Businessman in a suit standing before an open white door filled with bright light"></div>
  <h1 class="abs hero-title">GET A PREMIUM DOMAIN</h1>
  <p class="abs hero-sub">AND OPEN DOORS FOR NEW BUSINESS</p>
  <form class="abs search">
    <span class="abs search-input">Enter your domain name</span>
    <div class="abs tld-select">.com <svg width="12" height="8" style="margin-left:8px"><path d="M0 0h12L6 8z" fill="#666"/></svg></div>
    <div class="abs search-btn"><svg width="34" height="30" viewBox="0 0 34 30"><circle cx="12" cy="12" r="9" fill="none" stroke="#fff" stroke-width="3.5"/><path d="M19 18l11 9" stroke="#fff" stroke-width="5" stroke-linecap="round"/></svg></div>
  </form>
  <a class="abs adv-link">Advanced Search</a>
</section>

<div class="abs offer">
  <div class="abs offer-label">TODAY'S SPECIAL OFFER</div>
  <div class="abs offer-text">GET 25% OFF ON ALL PREMIUM DOMAINS</div>
  <div class="abs offer-btn">GRAB THE OFFER NOW</div>
</div>

<h2 class="abs section-title">DOMAINS FOR SALE</h2>
<table class="abs domain-table">
  <thead><tr><th>DOMAIN</th><th>CATEGORY</th><th>PRICE</th><th></th></tr></thead>
  <tbody>
    <tr><td class="name">medivella.com</td><td class="cat">Health</td><td class="price">$8700.00</td><td><span class="buy">Buy</span></td></tr>
    <tr><td class="name">trailpurses.com</td><td class="cat">Sports</td><td class="price">$5000.00</td><td><span class="buy">Buy</span></td></tr>
    <tr><td class="name">motors-vintaro.com</td><td class="cat">Vehicles</td><td class="price">$100.00</td><td><span class="buy">Buy</span></td></tr>
    <tr><td class="name">newcarvelo.com</td><td class="cat">Vehicles</td><td class="price">$100.00</td><td><span class="buy">Buy</span></td></tr>
    <tr><td class="name">sunetlibrix.com</td><td class="cat">Other</td><td class="price">$4397.00</td><td><span class="buy">Buy</span></td></tr>
    <tr><td class="name">everyhomestead.com</td><td class="cat">Real Estate</td><td class="price">$999.00</td><td><span class="buy">Buy</span></td></tr>
    <tr><td class="name">brief-q.com</td><td class="cat">Media</td><td class="price">$197.00</td><td><span class="buy">Buy</span></td></tr>
    <tr><td class="name">fabricadorestrela.com</td><td class="cat">Law</td><td class="price">$100.00</td><td><span class="buy">Buy</span></td></tr>
    <tr><td class="name">plainledgerhelp.com</td><td class="cat">Finance</td><td class="price">$300.00</td><td><span class="buy">Buy</span></td></tr>
    <tr><td class="name">zuvimo.com</td><td class="cat">Other</td><td class="price">$211.00</td><td><span class="buy">Buy</span></td></tr>
    <tr><td class="name">fit27.net</td><td class="cat">Other</td><td class="price">$999.00</td><td><span class="buy">Buy</span></td></tr>
    <tr><td class="name">refuelplanet.com</td><td class="cat">Society</td><td class="price">$100.00</td><td><span class="buy">Buy</span></td></tr>
  </tbody>
</table>
<div class="abs pager">‹ First « <b>1</b> 2 3 4 5 6 7 8 9 » &nbsp;Last ›</div>

<aside>
  <h3 class="abs testi-title">WHAT OUR CLIENT'S SAY</h3>
  <svg class="abs quote-mark" width="46" height="45" viewBox="0 0 46 45"><path d="M0 45V22C0 8 6 1 19 0v8c-6 1-8 5-8 11h8v26zM27 45V22C27 8 33 1 46 0v8c-6 1-8 5-8 11h8v26z" fill="#bdbdbd"/></svg>
  <div class="abs testi-who"><span>stillpose.example</span> says</div>
  <p class="abs testi-text">Excellent, responsive, service. The folks at Parcelwise Names Group are knowledgeable and the Parcelwise team made me sure that I was buying my domain from a trustworthy organiza-tion.</p>
</aside>

<footer class="abs site-footer">
  <div class="abs foot-links"><span>UNIVERSAL TERMS</span><span>REFUND POLICY</span><span>PRIVACY POLICY</span></div>
  <div class="abs foot-copy">© 2013 Zeprilo, Inc.</div>
  <div class="abs foot-addr">&nbsp;418 Larkmoor Street, Suite 12 Ashford Vale,<br>TN 37990 United States</div>
  <div class="abs foot-phone">+1 555.014.2290</div>
</footer>

</body>
</html>
```